Information One Page for Email

I am looking for a informative attachment I can send with an introductive email for Ridgeview Cable Works. Something I can also Mail.

Ridgeview Cable Works is the leader in Rebar Post Tension Cable Placement and Post Tension Cable repair. Outside of cable placement and repair we do concrete repair, Parking Garage restoration and

Content

Post Tension Repair and Concrete Restoration
Post-tensioning is a revolutionary method in concrete construction that enhances the strength and durability of structures. However, like all construction ele-ments, post-tension cables can experience wear and damage over time. Ensuring timely and effective repair is crucial for maintaining the safety and integrity of your building.
Why Post-Tension Cable Repair is Essential
1. **Structural Integrity**: Damaged or deteriorated cables can compromise the structural integrity of your building, leading to safety hazards and potential structural failures.
2. **Extended Lifespan**: Regular maintenance and repair of post-tension cables extend the lifespan of your structure, ensuring it remains safe and function-al for years to come.
3. **Cost-Effective**: Addressing cable issues early on prevents more severe damage and costly repairs down the line.
Common Signs of Post-Tension Cable Issues
- Cracks in concrete surfaces
- Unusual noises or popping sounds
- Visible cable ends or broken strands
- Water leakage through cracks
Our Repair Process
1. **Inspection and Assessment**: Our team conducts a thorough inspection to identify the extent of the damage and determine the appropriate repair meth-ods.
2. **Cable Repair or Replacement**: Depending on the severity, we either re-pair the existing cables or replace them with new ones to restore full functional-ity.
3. **Sealing and Protection**: After repairing, we seal the affected areas to protect against moisture and future damage.
4. **Quality Assurance**: We perform rigorous quality checks to ensure the repairs meet industry standards and the structure is safe for use.
Why Choose Us
- **Expertise and Experience**: With years of experience in post-tension cable repair, our team is skilled in handling even the most complex repairs efficiently and effectively.
- **Advanced Technology**: We use the latest technology and materials to ensure durable and long-lasting repairs.
- **Customer Satisfaction**: Our commitment to quality and customer satisfaction sets us apart. We work closely with our clients to ensure their needs are met and expectations exceeded.
Contact Us
If you suspect issues with your post-tension cables or need a routine inspection, don't hesitate to contact us. Our experts are ready to provide the best solutions to keep your structures safe and secure.
Ensure the safety and longevity of your building with our professional post-tension cable repair services. Trust us to deliver quality and reliability every time.

```html
<!DOCTYPE html>
<html lang="en">
<head>
<meta charset="utf-8">
<title>Ridgeview Cable Works – Post Tension Repair</title>
<link rel="stylesheet" href="https://fonts.googleapis.com/css2?family=Montserrat:wght@700;800&family=Manrope:wght@400;500;600;700;800&display=swap">
<style>
  :root {
    --green-deep: #0d5330;
    --green-dark: #14673a;
    --green-mid: #2f8a3f;
    --green-light: #7cc143;
    --gold: #c9a74e;
    --gold-light: #e9d9a6;
    --ink: #1c1c1c;
    --paper: #ffffff;
    --shade: #e4e4e4;
  }
  * { box-sizing: border-box; margin: 0; padding: 0; }
  html, body { width: 939px; height: 1200px; overflow: hidden; background: var(--paper); }
  body { position: relative; font-family: "Manrope", sans-serif; color: var(--ink); }

  .display { font-family: "Montserrat", sans-serif; font-weight: 800; }
  .gradient-text {
    background: linear-gradient(90deg, var(--green-deep) 0%, var(--green-dark) 35%, var(--gold) 100%);
    -webkit-background-clip: text; background-clip: text; color: transparent;
  }

  .brand { position: absolute; left: 38px; top: 52px; display: flex; align-items: center; gap: 9px; }
  .brand-square { width: 16px; height: 16px; background: var(--green-dark); }
  .brand-name { font-family: "Manrope", sans-serif; font-weight: 800; font-size: 19px; color: var(--green-dark); line-height: 1.1; width: 170px; }

  .header-band { position: absolute; left: 280px; right: 0; top: 62px; height: 40px;
    background: linear-gradient(180deg, rgba(255,255,255,0) 0%, var(--shade) 100%);
    border-top-left-radius: 60px 40px; }
  .site-url { position: absolute; right: 47px; top: 68px; font-weight: 700; font-size: 17px; color: var(--green-mid); letter-spacing: 0.2px; }

  .title { position: absolute; left: 46px; top: 128px; font-size: 43px; line-height: 45px; letter-spacing: -0.3px; }
  .intro { position: absolute; left: 442px; top: 162px; width: 430px; font-size: 14.3px; line-height: 24.3px; color: var(--green-mid); }

  .essential-shade { position: absolute; left: 0; right: 0; top: 336px; height: 70px;
    background: radial-gradient(ellipse at 50% 50%, #ececec 0%, rgba(255,255,255,0) 70%); }
  .essential-banner { position: absolute; left: 97px; top: 342px; width: 746px; height: 50px; }
  .essential-title { position: absolute; left: 0; width: 939px; top: 349px; text-align: center; font-size: 28.5px; color: var(--green-deep); }

  .benefit { position: absolute; top: 422px; display: flex; gap: 10px; }
  .benefit svg { flex: none; }
  .benefit h3 { font-weight: 800; font-size: 18px; color: var(--gold); margin-bottom: 2px; }
  .benefit p { font-size: 12.2px; line-height: 16.5px; color: var(--ink); }

  .signs { position: absolute; left: 0; top: 527px; width: 939px; height: 239px;
    background: linear-gradient(90deg, var(--green-light) 0%, var(--green-mid) 42%, var(--green-dark) 100%); overflow: hidden; }
  .signs-photo { position: absolute; left: 360px; top: 0; right: 0; bottom: 0;
    background: linear-gradient(100deg, rgba(47,138,63,0) 0%, rgba(34,130,70,0.7) 30%, #1f8a4c 60%, #136a3a 100%); }
  .signs-title { position: absolute; left: 46px; top: 54px; font-size: 34.5px; line-height: 40px; color: var(--paper); font-family: "Montserrat", sans-serif; font-weight: 700; }
  .sign-pill { position: absolute; height: 59px; border-radius: 30px; background: var(--gold);
    display: flex; align-items: center; justify-content: center; text-align: center;
    color: var(--paper); font-weight: 600; font-size: 18.5px; line-height: 21px; }

  .process-title { position: absolute; left: 50px; top: 793px; font-size: 29px; line-height: 32px; }
  .step { position: absolute; top: 795px; width: 163px; height: 96px; border-radius: 8px; padding: 10px 9px 0 9px; color: var(--paper); }
  .step h4 { font-weight: 800; font-size: 16.5px; line-height: 18.5px; margin-bottom: 8px; }
  .step p { font-size: 10.3px; line-height: 15px; color: rgba(255,255,255,0.85); }
  .step-1 { background: linear-gradient(90deg, var(--green-light), #5aa946); }
  .step-2 { background: #3b8a44; }
  .step-3 { background: #236f3c; }
  .step-4 { background: var(--green-deep); }
  .step-arrow { position: absolute; top: 826px; width: 35px; height: 35px; }

  .divider-shade { position: absolute; left: 55px; right: 22px; top: 906px; height: 26px;
    background: linear-gradient(180deg, var(--shade), rgba(255,255,255,0));
    border-radius: 50% 50% 0 0 / 100% 100% 0 0; }

  .choose-title { position: absolute; left: 0; width: 939px; top: 938px; text-align: center; font-size: 29px; }
  .reason { position: absolute; top: 978px; }
  .reason h3 { font-weight: 800; font-size: 17.8px; color: var(--gold); margin-bottom: 2px; }
  .reason p { font-size: 10.9px; line-height: 13.4px; color: var(--ink); }
  .reason-left { left: 70px; width: 254px; text-align: right; }
  .reason-center { left: 350px; width: 240px; text-align: center; }
  .reason-right { left: 614px; width: 270px; text-align: left; }

  .contact-title { position: absolute; left: 46px; top: 1088px; font-size: 29px; }
  .contact-text { position: absolute; left: 261px; top: 1086px; width: 640px; font-size: 12.2px; line-height: 17.8px; color: var(--ink); }
</style>
</head>
<body>

  <div class="header-band"></div>
  <div class="brand">
    <span class="brand-square"></span>
    <span class="brand-name">Ridgeview Cable Works</span>
  </div>
  <div class="site-url">www.ridgeviewcableworks.com</div>

  <h1 class="title display gradient-text">Post Tension<br>Repair and<br>Concrete<br>Restoration</h1>
  <p class="intro">Post-tensioning is a revolutionary method in concrete construction that enhances the strength and durability of structures. However, like all construction ele-ments, post-tension cables can experience wear and damage over time. Ensuring timely and effective repair is crucial for maintaining the safety and integrity of your building.</p>

  <div class="essential-shade"></div>
  <svg class="essential-banner" viewBox="0 0 746 50" preserveAspectRatio="none" aria-hidden="true">
    <defs>
      <linearGradient id="bannerGold" x1="0" x2="1" y1="0" y2="0">
        <stop offset="0" stop-color="#c9a74e"/>
        <stop offset="0.55" stop-color="#dcc383"/>
        <stop offset="1" stop-color="#f6efdc"/>
      </linearGradient>
    </defs>
    <path d="M0 0 H746 L722 38 Q714 50 700 50 H46 Q32 50 24 38 Z" fill="url(#bannerGold)"/>
  </svg>
  <h2 class="essential-title display">Why Post-Tension Cable Repair is Essential</h2>

  <div class="benefit" style="left:46px;">
    <svg width="76" height="78" viewBox="0 0 76 78" aria-hidden="true">
      <defs><linearGradient id="iconGrad1" x1="0" x2="1"><stop offset="0" stop-color="#0d5330"/><stop offset="1" stop-color="#7cc143"/></linearGradient></defs>
      <g fill="none" stroke="url(#iconGrad1)" stroke-width="4" stroke-linejoin="round">
        <path d="M8 74 V14 L46 2 V74"/>
        <path d="M46 30 H70 V74"/>
        <path d="M2 74 H74"/>
        <path d="M17 30 H36 M17 40 H36 M17 50 H36 M17 60 H36" stroke-linecap="round" stroke-width="4.5"/>
      </g>
    </svg>
    <div><h3>Structural Integrity</h3><p>Prevents compromised cables<br>from creating safety risks and<br>structural failure.</p></div>
  </div>

  <div class="benefit" style="left:344px;">
    <svg width="52" height="74" viewBox="0 0 52 74" aria-hidden="true" style="margin-right:4px">
      <defs><linearGradient id="iconGrad2" x1="0" x2="1" y1="0" y2="1"><stop offset="0" stop-color="#0d5330"/><stop offset="1" stop-color="#7cc143"/></linearGradient></defs>
      <g fill="none" stroke="url(#iconGrad2)" stroke-width="5" stroke-linecap="round" stroke-linejoin="round">
        <path d="M5 4 H47 Q47 24 28 37 Q47 50 47 70 H5 Q5 50 24 37 Q5 24 5 4 Z"/>
        <path d="M18 17 H34"/>
        <path d="M17 59 H35"/>
      </g>
    </svg>
    <div><h3>Extended Lifespan</h3><p>Routine repair helps maintain<br>long-term performance and<br>durability.</p></div>
  </div>

  <div class="benefit" style="left:615px;">
    <svg width="74" height="74" viewBox="0 0 74 74" aria-hidden="true">
      <defs><linearGradient id="iconGrad3" x1="0" x2="1" y1="1" y2="0"><stop offset="0" stop-color="#0d5330"/><stop offset="1" stop-color="#7cc143"/></linearGradient></defs>
      <g fill="none" stroke="url(#iconGrad3)" stroke-linecap="round" stroke-linejoin="round">
        <path d="M50 8 A32 32 0 1 0 68 32" stroke-width="5"/>
        <path d="M30 38 L43 50" stroke-width="0"/>
        <path d="M50 22 L58 30 L72 12" stroke-width="5"/>
        <path d="M44 26 Q40 21 34 21 Q25 21 25 28 Q25 34 34 36 Q43 38 43 45 Q43 52 34 52 Q27 52 24 47" stroke-width="6"/>
        <path d="M34 14 V59" stroke-width="5"/>
      </g>
    </svg>
    <div><h3>Cost-Effective</h3><p>Early intervention avoids major<br>damage and expensive future<br>repairs.</p></div>
  </div>

  <section class="signs">
    <div class="signs-photo" role="img" aria-label="Photo of post-tension cables and formwork tinted green"></div>
    <h2 class="signs-title">Common Signs of<br>Post-Tension<br>Cable Issues</h2>
    <div class="sign-pill" style="left:418px; top:50px; width:224px;">Cracks in concrete<br>surfaces</div>
    <div class="sign-pill" style="left:653px; top:48px; width:222px;">Unusual noises or<br>popping sounds</div>
    <div class="sign-pill" style="left:420px; top:131px; width:222px;">Visible cable ends<br>or broken strands</div>
    <div class="sign-pill" style="left:653px; top:129px; width:222px;">Water leakage<br>through cracks</div>
  </section>

  <h2 class="process-title display gradient-text">Our<br>Repair<br>Process</h2>
  <div class="step step-1" style="left:191px;"><h4>Inspection and Assessment</h4><p>Identify damage and define the right repair method.</p></div>
  <div class="step step-2" style="left:370px;"><h4>Cable Repair or Replacement</h4><p>Restore full structural performance.</p></div>
  <div class="step step-3" style="left:550px;"><h4>Sealing<br>&amp; Protection</h4><p>revent moisture and future deterioration.</p></div>
  <div class="step step-4" style="left:729px;"><h4>Quality<br>Assurance</h4><p>Verified to meet industry standards.</p></div>

  <svg class="step-arrow" style="left:345px;" viewBox="0 0 35 35" aria-hidden="true">
    <defs><radialGradient id="arrowGold" cx="0.4" cy="0.4" r="0.7"><stop offset="0" stop-color="#f7efd7"/><stop offset="1" stop-color="#c9a74e"/></radialGradient></defs>
    <circle cx="17.5" cy="17.5" r="17.5" fill="url(#arrowGold)"/>
    <path d="M14 9 L22 17.5 L14 26" fill="none" stroke="#0d5330" stroke-width="4" stroke-linecap="round" stroke-linejoin="round"/>
  </svg>
  <svg class="step-arrow" style="left:524px;" viewBox="0 0 35 35" aria-hidden="true">
    <circle cx="17.5" cy="17.5" r="17.5" fill="url(#arrowGold)"/>
    <path d="M14 9 L22 17.5 L14 26" fill="none" stroke="#0d5330" stroke-width="4" stroke-linecap="round" stroke-linejoin="round"/>
  </svg>
  <svg class="step-arrow" style="left:703px;" viewBox="0 0 35 35" aria-hidden="true">
    <circle cx="17.5" cy="17.5" r="17.5" fill="url(#arrowGold)"/>
    <path d="M14 9 L22 17.5 L14 26" fill="none" stroke="#0d5330" stroke-width="4" stroke-linecap="round" stroke-linejoin="round"/>
  </svg>

  <div class="divider-shade"></div>

  <h2 class="choose-title display"><span class="gradient-text">Why Choose Us</span></h2>
  <div class="reason reason-left"><h3>Expertise and Experience</h3><p>With years of experience in post-tension cable repair, our team is skilled in handling even the most complex repairs efficiently and effectively.</p></div>
  <div class="reason reason-center"><h3>Advanced Technology</h3><p>We use the latest technology and materials to ensure durable and long-lasting repairs.</p></div>
  <div class="reason reason-right"><h3>Customer Satisfaction</h3><p>Our commitment to quality and customer satisfaction sets us apart. We work closely with our clients to ensure their needs are met and expectations exceeded</p></div>

  <h2 class="contact-title display"><span class="gradient-text">Contact Us</span></h2>
  <p class="contact-text">If you suspect issues with your post-tension cables or need a routine inspection, don’t hesitate to contact us. Our experts are ready to provide the best solutions to keep your structures safe and secure.<br>Ensure the safety and longevity of your building with our professional post-tension cable repair services. Trust us to deliver quality and reliability every time.</p>

</body>
</html>
```